Book Cover - For Best Selling Diet

Hi
Book cover required for a diet book being marketed to become a best seller
For best quality, image will be 2820 pixels on the shortest side and 4500 pixels on the longest side .
The book name : Bright Morning Plan
By Corinna Plett
( will add in the extra text once we see design - top and bottom subtitle )
I do not want a photo of a person on the book.
PLEASE SEE " THE 9 STEP FRAME" by Ned Galbury as an example of solid style and I also love Quiet Ledger for the font.
Branding Colours:
#F26432
#A4195C
#A7D8CC
Font that runs through our brand is : helvetica neue
This is for a book that will be marketed for #1 bestseller - So please only quality
designs that are designed in a unique style.
Thanks
Target Market(s)
Busy Working Mums, Affluent, 30+ .
Look and feel

```html
<!DOCTYPE html>
<html lang="en">
<head>
<meta charset="utf-8">
<title>Bright Morning Plan – Book Cover</title>
<link rel="stylesheet" href="https://fonts.googleapis.com/css2?family=Arimo:wght@400&display=swap">
<style>
  :root {
    --brand-orange: #F26432;
    --brand-magenta: #A4195C;
    --brand-mint: #A7D8CC;
    --cover-glow: #45132f;
    --cover-mid: #2e0b22;
    --cover-deep: #170510;
    --stage: #1a0913;
    --title-font: "Arimo", "Helvetica Neue", Helvetica, Arial, sans-serif;
  }

  html, body {
    margin: 0;
    padding: 0;
    width: 1200px;
    height: 1000px;
    overflow: hidden;
    background: var(--stage);
  }

  .canvas {
    position: relative;
    width: 1200px;
    height: 1000px;
    display: flex;
    align-items: center;
    justify-content: center;
  }

  .book-cover {
    position: relative;
    width: 626px;
    height: 934px;
    overflow: hidden;
    box-shadow: 0 0 0 2px #0c0308, 0 18px 40px rgba(0, 0, 0, 0.6);
  }

  .cover-surface {
    position: absolute;
    inset: 0;
    background:
      radial-gradient(ellipse 70% 45% at 52% 32%, rgba(120, 30, 80, 0.35) 0%, rgba(120, 30, 80, 0) 100%),
      radial-gradient(ellipse 120% 90% at 50% 40%, var(--cover-glow) 0%, var(--cover-mid) 50%, var(--cover-deep) 100%);
  }

  .cover-surface::after {
    content: "";
    position: absolute;
    inset: 0;
    background: linear-gradient(180deg, rgba(0, 0, 0, 0) 55%, rgba(0, 0, 0, 0.35) 100%),
                linear-gradient(90deg, rgba(0, 0, 0, 0.25) 0%, rgba(0, 0, 0, 0) 20%, rgba(0, 0, 0, 0) 80%, rgba(0, 0, 0, 0.25) 100%);
  }

  .top-band {
    position: absolute;
    top: 0;
    left: 0;
    right: 0;
    height: 24px;
    background: var(--brand-magenta);
  }

  .title {
    position: absolute;
    top: 158px;
    left: 0;
    right: 0;
    margin: 0;
    text-align: center;
    font-family: var(--title-font);
    font-weight: 400;
    line-height: 1;
  }

  .title-lead {
    display: block;
    font-size: 146px;
    color: var(--brand-orange);
    letter-spacing: -2px;
    text-shadow: 4px 5px 6px rgba(0, 0, 0, 0.8);
  }

  .title-rest {
    display: block;
    margin-top: 6px;
    font-size: 92px;
    color: var(--brand-mint);
    letter-spacing: -2px;
    text-shadow: 4px 5px 6px rgba(0, 0, 0, 0.8);
  }

  .author-band {
    position: absolute;
    left: 0;
    right: 0;
    bottom: 0;
    height: 64px;
    background: var(--brand-magenta);
    display: flex;
    align-items: center;
    justify-content: flex-end;
    padding-right: 44px;
    box-sizing: border-box;
  }

  .author-name {
    font-family: var(--title-font);
    font-size: 46px;
    color: var(--brand-mint);
    letter-spacing: -1px;
  }
</style>
</head>
<body>
  <main class="canvas">
    <article class="book-cover">
      <div class="cover-surface" role="img" aria-label="Deep plum cover surface; a fine honeycomb texture belongs here across the whole cover"></div>
      <div class="top-band"></div>
      <h1 class="title">
        <span class="title-lead">Bright</span>
        <span class="title-rest">Morning Plan</span>
      </h1>
      <footer class="author-band">
        <span class="author-name">Corinna Plett</span>
      </footer>
    </article>
  </main>
</body>
</html>
```